Design required for boutique fire engineering firm in New Zealand

Our website was published based on free Wordpress templates, we'd like something a bit more bespoke, clean and simple.
Updates

Reason: didn't check this finished on a Sunday :)

Target Market(s)

architects, building owners, property developers

Industry/Entity Type

Boutique

Contact Information for Business Card

Logo
Fire Engineering

Desmond Harlow
Principal
+64 21 482 735
desmond@veltrane.nz
veltrane.nz

Number of Pages Required

3 page

Font styles to use
Sans Serif

Requirements
Nice to have
• On the business card, an embossed logo would be great - not sure if that's a design thing or just a print thing?
• Website, existing @ http://veltrane.nz for extent of content and general arrangement that I'm happy with.
• Ability to update the content with project bio's and some photos at a later date would be nice.

```html
<!DOCTYPE html>
<html lang="en">
<head>
<meta charset="utf-8">
<title>Veltrane – Fire Engineering</title>
<link href="https://fonts.googleapis.com/css2?family=Lato:wght@400;700;900&display=swap" rel="stylesheet">
<style>
:root{
  --blue:#2f6db5;
  --blue-deep:#1d5aa0;
  --navy:#0e4b7c;
  --ink:#222;
  --muted:#555;
  --bar:#1c1c1c;
  --grey:#efefef;
  --white:#fff;
}
*{box-sizing:border-box;margin:0;padding:0}
html,body{width:1200px;height:3930px;overflow:hidden}
body{font-family:"Lato",sans-serif;color:var(--ink);background:var(--white);position:relative}
.abs{position:absolute}
.center{text-align:center}

/* top bar */
.topbar{position:absolute;top:0;left:0;width:1200px;height:24px;background:var(--bar);color:#ddd;font-size:12px}
.topbar .mail{left:120px;top:5px}
.topbar .call{left:0;width:1200px;top:5px;text-align:center}
.topbar .social{right:120px;top:6px;display:flex;gap:14px}
.topbar .social span{width:12px;height:12px;background:#ddd;border-radius:2px}

/* header */
.header{position:absolute;top:24px;left:0;width:1200px;height:126px;background:var(--white)}
.brand{position:absolute;left:120px;top:34px;display:flex;align-items:center;gap:12px}
.brand .dot{width:56px;height:56px;border-radius:50%;background:var(--blue-deep)}
.brand .name{font-size:44px;font-weight:700;color:var(--blue-deep);letter-spacing:-1px}
.nav{position:absolute;left:543px;top:54px;display:flex;gap:22px;font-size:14px;font-weight:700;color:#333}
.nav .active{color:var(--blue-deep);border-bottom:2px solid var(--blue-deep);padding-bottom:4px}
.quote{position:absolute;left:936px;top:44px;width:146px;height:36px;background:var(--navy);color:#fff;border-radius:6px;font-weight:700;font-size:15px;display:flex;align-items:center;justify-content:center}

/* hero */
.hero{position:absolute;top:150px;left:0;width:1200px;height:596px;background:linear-gradient(180deg,#6f7e92 0%,#8d9bab 35%,#4d5a66 65%,#36424d 100%)}
.hero h1{position:absolute;top:252px;width:1200px;text-align:center;color:#fff;font-size:38px;line-height:44px;font-weight:700;letter-spacing:1px}
.hero p{position:absolute;top:342px;width:1200px;text-align:center;color:#fff;font-size:15px;line-height:20px}
.btn{display:flex;align-items:center;justify-content:center;background:var(--blue);color:#fff;font-size:15px;font-weight:700;border-radius:2px}
.hero .btn{position:absolute;left:532px;top:394px;width:136px;height:38px}

/* audience cards */
.audience{position:absolute;top:665px;left:157px;width:886px;height:231px;background:var(--grey);display:flex;box-shadow:0 2px 6px rgba(0,0,0,.15)}
.audience .item{flex:1;text-align:center;padding-top:22px;border-right:1px solid #ccc;margin:24px 0}
.audience .item:last-child{border-right:0}
.audience .item{padding-top:0}
.audience svg{width:52px;height:52px}
.audience h3{font-size:15px;font-weight:900;margin:8px 0 14px}
.audience p{font-size:14px;line-height:17px;color:#333;width:210px;margin:0 auto}
.more{font-size:14px;color:#333;margin-top:6px}
.more i{display:inline-block;width:12px;height:12px;border-radius:50%;border:1.5px solid var(--blue);vertical-align:-2px;margin-left:3px}

/* consulting */
.consult h2{position:absolute;top:950px;width:1200px;text-align:center;font-size:26px;font-weight:900}
.consult p{position:absolute;top:1008px;left:180px;width:840px;text-align:center;font-size:15px;line-height:18px;color:#333}
.consult .btn{position:absolute;left:532px;top:1108px;width:136px;height:37px}

.rule{width:38px;height:4px;background:currentColor;margin:12px auto 0}

/* what we do */
.services{position:absolute;top:1192px;left:0;width:1200px;height:611px;background:var(--blue);color:#fff}
.sec-title{position:absolute;width:1200px;text-align:center;font-size:26px;font-weight:900}
.sec-sub{position:absolute;width:1200px;text-align:center;font-size:14px;font-weight:700}
.services .cards .card{position:absolute;top:183px;height:360px;background:#fff;color:var(--ink);text-align:center}
.photo{display:block;width:100%}
.services .card .photo{height:200px}
.services .card h3{font-size:16px;font-weight:900;margin-top:20px}
.services .card .rule{width:36px;height:4px;background:#222;margin:10px auto 14px}
.services .card p{font-size:14px;line-height:17px;width:220px;margin:0 auto}
.services .card i{display:block;width:16px;height:16px;border-radius:50%;border:2px solid var(--blue);margin:12px auto 0}

/* projects */
.projects{position:absolute;top:1803px;left:0;width:1200px;height:830px}
.projects .sec-title{color:var(--ink)}
.projects .sec-sub{color:#333}
.tabs{position:absolute;top:167px;left:312px;display:flex;align-items:center;font-size:15px;font-weight:700}
.tabs span{padding:0 28px;height:34px;display:flex;align-items:center}
.tabs .on{background:var(--blue);color:#fff;width:164px;justify-content:center}
.tile{position:absolute}
.tile.logo{background:var(--blue);display:flex;align-items:center;justify-content:center;gap:12px;color:#fff;font-size:40px;font-weight:700}
.tile.logo span{width:40px;height:40px;border-radius:50%;background:#fff}
.projects .btn{position:absolute;left:532px;top:736px;width:136px;height:39px}

/* blog */
.blog{position:absolute;top:2633px;left:0;width:1200px;height:611px;background:var(--blue);color:#fff}
.post{position:absolute;top:147px;width:306px}
.post .photo{height:194px;position:relative}
.post .date{position:absolute;top:0;right:0;width:40px;height:40px;background:var(--blue);font-size:14px;font-weight:900;text-align:center;line-height:16px;padding-top:4px}
.post .date small{display:block;font-size:10px;font-weight:400}
.post h3{font-size:15px;font-weight:900;margin-top:18px}
.post .meta{font-size:13px;margin-top:5px;display:flex;justify-content:space-between;padding-right:40px}
.post p{font-size:14px;line-height:16px;margin-top:18px}
.post .more{color:#fff;margin-top:4px}
.post .more i{border-color:#fff}
.blog .ghost{position:absolute;left:532px;top:519px;width:136px;height:39px;background:#fff;color:var(--ink);font-size:15px;font-weight:700;display:flex;align-items:center;justify-content:center}

/* newsletter */
.news h2{position:absolute;top:3378px;width:1200px;text-align:center;font-size:24px;font-weight:900;letter-spacing:1px}
.news p{position:absolute;top:3410px;width:1200px;text-align:center;font-size:14px;letter-spacing:1.5px;color:#333}
.news .field{position:absolute;top:3458px;left:354px;width:394px;height:24px;border:1px solid #ccc;font-size:11px;color:#999;padding:5px 6px}
.news .send{position:absolute;top:3458px;left:750px;width:90px;height:24px;background:var(--blue-deep);color:#fff;font-size:14px;font-weight:900;display:flex;align-items:center;justify-content:center;letter-spacing:1px}

/* footer */
.footer{position:absolute;top:3608px;left:0;width:1200px;height:272px;background:var(--navy);color:#fff}
.footer .col{position:absolute;top:56px}
.footer h4{font-size:15px;font-weight:700;margin-bottom:18px}
.footer .fbrand{display:flex;align-items:center;gap:8px;font-size:26px;font-weight:700;margin-bottom:14px}
.footer .fbrand span{width:24px;height:24px;border-radius:50%;background:#fff}
.footer .about{font-size:14px;line-height:18px;color:#9fb6cc;width:210px}
.footer ul{list-style:none;font-size:14px;line-height:25px}
.footer li::before{content:"›";margin-right:10px;font-weight:700}
.footer .contact{font-size:14px;line-height:24px;color:#c5d4e2}
.qc input,.qc .box{background:transparent;border:1px solid #9fb6cc;color:#c5d4e2;font:12px "Lato",sans-serif;padding:2px 4px}
.qc .row{display:flex;gap:4px;margin-bottom:8px}
.qc .row input{width:98px;height:20px}
.qc .box{width:200px;height:50px;margin-bottom:8px}
.qc .sendb{width:200px;height:20px;background:var(--blue);font-size:11px;font-weight:700;display:flex;align-items:center;justify-content:center}
.bottombar{position:absolute;top:3880px;left:0;width:1200px;height:50px;background:var(--bar);color:#fff;font-size:14px;font-weight:700}
.bottombar .links{position:absolute;left:120px;top:16px}
</style>
</head>
<body>

<div class="topbar">
  <div class="abs mail">info@veltrane.nz</div>
  <div class="abs call">CALL US : 123 456 7890</div>
  <div class="abs social"><span></span><span></span><span></span><span></span><span></span></div>
</div>

<header class="header">
  <div class="brand"><span class="dot"></span><span class="name">veltrane</span></div>
  <nav class="nav">
    <span class="active">HOME</span><span>ABOUT US</span><span>PROJECTS</span><span>BLOG</span><span>CONTACT US</span>
  </nav>
  <div class="quote">Get a Quote</div>
</header>

<section class="hero" role="img" aria-label="City skyline with a tall tower over the harbour under a cloudy sky">
  <h1>FIRE ENGINEERING<br>THOUGHTFUL, RESPONSIVE</h1>
  <p>Lorem Ipsum is simply dummy text of the printing and industry.<br>Lorem Ipsum has been the industry's</p>
  <div class="btn">Read More</div>
</section>

<section class="audience">
  <div class="item">
    <svg viewBox="0 0 52 52" fill="none" stroke="#1d5aa0" stroke-width="3"><circle cx="26" cy="8" r="4"/><path d="M24 12 12 46M28 12l12 34M14 32c8 5 16 5 24 0"/></svg>
    <h3>ARCHITECTS</h3>
    <p>Lorem Ipsum is simply dummy text of the printing and the typesetting industry</p>
    <div class="more">Read More.. <i></i></div>
  </div>
  <div class="item">
    <svg viewBox="0 0 52 52" fill="none" stroke="#1d5aa0" stroke-width="3"><path d="M6 48h40M12 48V18h12v30M24 48V6h14v42M16 24h4M16 32h4M16 40h4M29 14h4M29 22h4M29 30h4M29 38h4"/></svg>
    <h3>BUILDING OWNERS</h3>
    <p>Lorem Ipsum is simply dummy text of the printing and the typesetting industry</p>
    <div class="more">Read More.. <i></i></div>
  </div>
  <div class="item">
    <svg viewBox="0 0 52 52" fill="none" stroke="#1d5aa0" stroke-width="3"><path d="M4 26 26 6l22 20M10 21v25h32V21M20 36c4 4 8 4 12 0M40 8v8"/></svg>
    <h3>PROPERTY DEVELOPERS</h3>
    <p>Lorem Ipsum is simply dummy text of the printing and the typesetting industry</p>
    <div class="more">Read More.. <i></i></div>
  </div>
</section>

<section class="consult">
  <h2>CONSULTING FIRE ENGINEERS</h2>
  <p>Veltrane is a boutique fire engineering firm based in Wellington, New Zealand, founded by Desmond Harlow in 2017. We provide consulting services in the built environment, including design and review services to assist in Building Consent applications, advice on property protection matters, observation of construction on site, and regulatory consultation.</p>
  <div class="btn">Read More</div>
</section>

<section class="services">
  <h2 class="sec-title" style="top:76px">WHAT WE DO<div class="rule" style="background:#fff"></div></h2>
  <p class="sec-sub" style="top:132px">Lorem Ipsum is simply dummy text of the printing and of thebtypesetting industry</p>
  <div class="cards">
    <div class="card" style="left:115px;width:315px">
      <div class="photo" role="img" aria-label="Two engineers in hard hats reviewing plans inside a building under construction" style="background:linear-gradient(135deg,#c9ccd1,#8f959c 60%,#b07a3e)"></div>
      <h3>ARCHITECTS</h3><div class="rule"></div>
      <p>Lorem Ipsum is simply dummy text of the printing and of the typesetting industry</p><i></i>
    </div>
    <div class="card" style="left:443px;width:314px">
      <div class="photo" role="img" aria-label="Glass office towers seen from below against the sky" style="background:linear-gradient(160deg,#9fb6c9,#3f5569 55%,#22303d)"></div>
      <h3>BUILDING</h3><div class="rule"></div>
      <p>Lorem Ipsum is simply dummy text of the printing and of the typesetting industry</p><i></i>
    </div>
    <div class="card" style="left:773px;width:309px">
      <div class="photo" role="img" aria-label="White apartment buildings with balconies" style="background:linear-gradient(160deg,#e4e8ec,#aeb6be 60%,#7f8891)"></div>
      <h3>PROPERTY DEVELOPERS</h3><div class="rule"></div>
      <p>Lorem Ipsum is simply dummy text of the printing and of the typesetting industry</p><i></i>
    </div>
  </div>
</section>

<section class="projects">
  <h2 class="sec-title" style="top:75px">OUR PROJECTS<div class="rule" style="background:#222"></div></h2>
  <p class="sec-sub" style="top:128px">Lorem Ipsum is simply dummy text of the printing and of thebtypesetting industry</p>
  <div class="tabs"><span class="on">ARCHITECTS</span><span>BUILDING OWNERS</span><span>PROPERTY</span><span>OTHER</span></div>
  <div class="tile" role="img" aria-label="Modern waterfront building at dusk" style="left:120px;top:219px;width:470px;height:231px;background:linear-gradient(180deg,#4a525a,#2b3036)"></div>
  <div class="tile" role="img" aria-label="Dark patterned building facade" style="left:603px;top:219px;width:235px;height:231px;background:linear-gradient(160deg,#5b4530,#2a221b)"></div>
  <div class="tile" role="img" aria-label="Workers in hard hats on a site" style="left:846px;top:219px;width:236px;height:231px;background:linear-gradient(160deg,#6a5e55,#3b3733)"></div>
  <div class="tile" role="img" aria-label="Lit glass building at night" style="left:120px;top:461px;width:239px;height:236px;background:linear-gradient(180deg,#3a4147,#23282c)"></div>
  <div class="tile" role="img" aria-label="Firefighter in breathing apparatus" style="left:367px;top:461px;width:471px;height:236px;background:linear-gradient(160deg,#3c3c3c,#1e1e1e)"></div>
  <div class="tile logo" style="left:844px;top:461px;width:238px;height:236px;font-size:32px"><span></span>veltrane</div>
  <div class="btn">View More</div>
</section>

<section class="blog">
  <h2 class="sec-title" style="top:58px">OUR BLOG<div class="rule" style="background:#fff"></div></h2>
  <p class="sec-sub" style="top:112px">Lorem Ipsum is simply dummy text of the printing and of thebtypesetting industry</p>
  <article class="post" style="left:118px">
    <div class="photo" role="img" aria-label="Firefighter in front of flames" style="background:linear-gradient(135deg,#3a2412,#c2621d 55%,#f0a23a)"><div class="date">21<small>Nov</small></div></div>
    <h3>ARCHITECTURE INVESTMENT</h3>
    <div class="meta"><span>◌ November 02, 2017</span><span>♡ 12</span></div>
    <p>Lorem Ipsum is simply dummy text of the printing and typesetting industry. Lorem dummy text ever since the 1500s,</p>
    <div class="more">Read More <i></i></div>
  </article>
  <article class="post" style="left:445px">
    <div class="photo" role="img" aria-label="Firefighters working near a blaze" style="background:linear-gradient(135deg,#2c1a10,#b5511a 55%,#e8913a)"><div class="date">22<small>Nov</small></div></div>
    <h3>BUILDING GUIDE LINE INVESTMENT</h3>
    <div class="meta"><span>◌ November 02, 2017</span><span>♡ 12</span></div>
    <p>Lorem Ipsum is simply dummy text of the printing and typesetting industry. Lorem dummy text ever since the 1500s,</p>
    <div class="more">Read More <i></i></div>
  </article>
  <article class="post" style="left:773px">
    <div class="photo" role="img" aria-label="Firefighter in protective gear amid fire" style="background:linear-gradient(135deg,#34200f,#c0601e 55%,#eca03f)"><div class="date">23<small>Nov</small></div></div>
    <h3>PORPERTY INVESTMENT</h3>
    <div class="meta"><span>◌ November 02, 2017</span><span>♡ 12</span></div>
    <p>Lorem Ipsum is simply dummy text of the printing and typesetting industry. Lorem dummy text ever since the 1500s,</p>
    <div class="more">Read More <i></i></div>
  </article>
  <div class="ghost">View More</div>
</section>

<section class="news">
  <h2>SUBSCRIBE TO OUR NEWSLETTER</h2>
  <p>TO RECEIVE THE LATEST NEWS &amp; UPDATE</p>
  <div class="field">Your Mail</div>
  <div class="send">SUBMIT</div>
</section>

<footer class="footer">
  <div class="col" style="left:120px;top:52px">
    <div class="fbrand"><span></span>veltrane</div>
    <p class="about">Lorem Ipsum is simply dummy text of the printing and type setting industry has been the industry's <span style="color:#fff">→</span></p>
  </div>
  <div class="col" style="left:397px">
    <h4>Quick Links</h4>
    <ul><li>Home</li><li>About us</li><li>Projects</li><li>Blog</li><li>Contact us</li></ul>
  </div>
  <div class="col" style="left:638px">
    <h4>Contact Info</h4>
    <div class="contact">P: 123 456 7890<br>F: 123 456 7890<br><br>info@veltrane.com<br><br>12345 West 12th Street,<br>Suite 123, Country.</div>
  </div>
  <div class="col qc" style="left:870px">
    <h4>Quick Contact</h4>
    <div class="row"><input value="Name"><input value="Email"></div>
    <div class="box">Message</div>
    <div class="sendb">SEND</div>
  </div>
</footer>

<div class="bottombar"><div class="links">Privacy policy - Legal Mentions - Terms and Conditions</div></div>

</body>
</html>
```